Super Creative! Pixel Foundry Ad

CREATIVE CREATIVE CREATIVE needed for our Ad that will be placed on Google Ads, in print and on billboards. Our website is https://mypixelfoundry.example

Target Market(s)

B2B

Requirements
Must have
• Uniqueness, creative and the following marks and copy:
1. our logo
2. Our phone number: (555) 274-0386
3. Our website address: mypixelfoundry.example
4. Main message: BUILD BRAND. SUSTAIN GROWTH CURVE.

```html
<!DOCTYPE html>
<html lang="en">
<head>
<meta charset="utf-8">
<title>Pixel Foundry Ad Set</title>
<link href="https://fonts.googleapis.com/css2?family=Hind:wght@400;600;700&family=Montserrat:wght@400&family=Oswald:wght@600&display=swap" rel="stylesheet">
<style>
:root{
  --board:#666666;
  --label:#b3b3b3;
  --sky-top:#dfe3e8;
  --sky-bottom:#e8edf1;
  --blue-light:#5ccbf5;
  --blue:#1a8ee0;
  --blue-deep:#0f6fd1;
  --navy:#0b2a78;
  --ink:#1b1b1b;
  --paper:#f1f2f4;
  --band:#1d1e20;
  --photo-a:#f4f1f1;
  --photo-b:#dfe4e2;
}
*{margin:0;padding:0;box-sizing:border-box}
html,body{width:1200px;height:2406px;overflow:hidden}
body{background:var(--board);font-family:"Hind",sans-serif;position:relative}
.section-label{position:absolute;left:0;width:1200px;text-align:center;font-family:"Montserrat",sans-serif;font-weight:400;font-size:56px;color:var(--label);letter-spacing:1px}
.brand{display:flex;align-items:center;gap:10px;font-weight:700;color:var(--ink);text-transform:uppercase;white-space:nowrap}
.brand-mark{background:var(--ink);flex:none}
.icon{flex:none}

/* square ad */
.ad-square{position:absolute;left:325px;top:157px;width:548px;height:457px;background:linear-gradient(135deg,#fafafa,#e9eaec);overflow:hidden}
.ad-square svg.shape{position:absolute;left:0;top:0}
.ad-square .brand{position:absolute;top:32px;left:0;width:100%;justify-content:center;font-size:27px}
.ad-square .brand-mark{width:26px;height:26px}
.ad-square .headline{position:absolute;top:92px;left:0;width:100%;text-align:center;color:#fff;font-weight:700;line-height:1}
.headline .l1{display:block;font-size:58px}
.headline .l2{display:block;font-size:86px;margin-top:-4px}
.headline .l3{display:block;font-size:46px;margin-top:-6px}
.contact{display:flex;align-items:center;gap:8px;font-weight:600;color:var(--ink);white-space:nowrap}
.contact .divider{width:3px;background:var(--blue);align-self:stretch;margin:0 6px}
.ad-square .contact{position:absolute;top:400px;left:26px;font-size:25px;height:36px}

/* leaderboard */
.ad-wide{position:absolute;left:136px;top:666px;width:928px;height:162px;background:linear-gradient(135deg,#fafafa,#e6e8ea);overflow:hidden}
.ad-wide svg.shape{position:absolute;left:0;top:0}
.ad-wide .headline{position:absolute;left:80px;top:28px;color:#fff;line-height:1}
.ad-wide .l1{font-weight:700;font-size:60px}
.ad-wide .l2{font-family:"Oswald",sans-serif;font-weight:600;font-size:38px;margin-top:-2px;letter-spacing:.3px}
.ad-wide .brand{position:absolute;left:648px;top:26px;font-size:25px}
.ad-wide .brand-mark{width:24px;height:24px}
.phone-pill{position:absolute;left:644px;top:82px;width:250px;height:38px;border-radius:19px;background:linear-gradient(90deg,var(--blue-light),var(--blue-deep));display:flex;align-items:center;gap:10px;padding-left:6px;color:#fff;font-size:27px;font-weight:400}
.phone-pill .icon{background:#fff;border-radius:50%}
.ad-wide .site{position:absolute;left:652px;top:122px;font-size:16px;letter-spacing:3.4px;color:var(--ink)}

/* billboard */
.billboard{position:absolute;width:891px;height:355px;background:linear-gradient(135deg,#fbfbfc,#e7e8ea);overflow:hidden}
.billboard .band{position:absolute;left:0;bottom:0;width:100%;height:77px;background:var(--band)}
.billboard svg.shape{position:absolute;left:0;top:0}
.billboard .brand{position:absolute;left:62px;top:24px;font-size:34px}
.billboard .brand-mark{width:32px;height:32px}
.billboard .headline{position:absolute;left:58px;top:98px;color:var(--ink);font-weight:700;line-height:1}
.billboard .l1{font-size:52px}
.billboard .l2{font-size:74px;margin-top:-4px;background:linear-gradient(90deg,var(--blue-light),var(--blue-deep));-webkit-background-clip:text;background-clip:text;color:transparent}
.billboard .l3{font-size:42px;margin-top:-6px}
.billboard .contact{position:absolute;left:48px;bottom:20px;color:#fff;font-size:25px;height:36px}
.billboard .contact .site{font-weight:400;font-size:23px}
.flat-billboard{left:154px;top:1072px}

.scene{position:absolute;left:0;top:1525px;width:1200px;height:881px;background:linear-gradient(180deg,var(--sky-top),var(--sky-bottom))}
.scene .billboard{left:154px;top:263px;transform:scale(1.12);transform-origin:center}
</style>
</head>
<body>

<div class="section-label" style="top:42px">Google ad</div>

<section class="ad-square">
  <svg class="shape" width="548" height="457" viewBox="0 0 548 457">
    <defs><linearGradient id="sqBlue" x1="0" y1="0" x2="0.4" y2="1"><stop offset="0" stop-color="#5ccbf5"/><stop offset="1" stop-color="#0f6fd1"/></linearGradient></defs>
    <polygon points="0,0 548,0 548,290 260,372 0,290" fill="#0b2a78"/>
    <polygon points="0,0 548,0 548,278 260,352 0,278" fill="url(#sqBlue)"/>
  </svg>
  <div class="brand"><span class="brand-mark"></span>Pixel Foundry</div>
  <h1 class="headline"><span class="l1">BUILD BRAND</span><span class="l2">SUSTAIN</span><span class="l3">GROWTH CURVE</span></h1>
  <div class="contact">
    <svg class="icon" width="28" height="28" viewBox="0 0 28 28"><circle cx="14" cy="14" r="12" fill="none" stroke="#1a8ee0" stroke-width="2.5"/><path d="M9 8l3 0 1 4-2 1.5a8 8 0 0 0 3.5 3.5L16 15l4 1v3a1.5 1.5 0 0 1-1.5 1.5A11 11 0 0 1 7.5 9.5 1.5 1.5 0 0 1 9 8z" fill="#1a8ee0"/></svg>
    <span>(555) 274-0386</span><span class="divider"></span>
    <svg class="icon" width="26" height="26" viewBox="0 0 26 26"><circle cx="13" cy="13" r="11" fill="none" stroke="#1a8ee0" stroke-width="2.5"/><circle cx="13" cy="13" r="7" fill="#1a8ee0"/><path d="M6 13h14M13 6v14" stroke="#fff" stroke-width="1.2"/></svg>
    <span style="font-weight:400;font-size:23px">mypixelfoundry.example</span>
  </div>
</section>

<section class="ad-wide">
  <svg class="shape" width="928" height="162" viewBox="0 0 928 162">
    <defs><linearGradient id="wideBlue" x1="0" y1="0" x2="1" y2="0"><stop offset="0" stop-color="#5ccbf5"/><stop offset="1" stop-color="#0f6fd1"/></linearGradient></defs>
    <polygon points="0,0 612,0 552,162 0,162" fill="#0b2a78"/>
    <polygon points="0,0 585,0 545,162 0,162" fill="url(#wideBlue)"/>
  </svg>
  <div class="headline"><div class="l1">BUILD BRAND</div><div class="l2">SUSTAIN GROWTH CURVE</div></div>
  <div class="brand"><span class="brand-mark"></span>Pixel Foundry</div>
  <div class="phone-pill">
    <svg class="icon" width="30" height="30" viewBox="0 0 28 28"><path d="M9 7l3 0 1 4-2 1.5a8 8 0 0 0 3.5 3.5L16 14l4 1v3a1.5 1.5 0 0 1-1.5 1.5A11 11 0 0 1 7.5 8.5 1.5 1.5 0 0 1 9 7z" fill="#1b1b1b"/></svg>
    <span>(555) 274-0386</span>
  </div>
  <div class="site">mypixelfoundry.example</div>
</section>

<div class="section-label" style="top:967px">Billboard</div>

<section class="billboard flat-billboard">
  <div class="band"></div>
  <svg class="shape" width="891" height="355" viewBox="0 0 891 355">
    <defs><linearGradient id="photoTone" x1="0" y1="0" x2="1" y2="1"><stop offset="0" stop-color="#f4f1f1"/><stop offset="1" stop-color="#dfe4e2"/></linearGradient></defs>
    <polygon points="615,0 410,96 580,355 600,355 445,100 655,0" fill="#0b2a78"/>
    <polygon points="640,0 430,98 596,355 616,355 458,102 670,0" fill="#1a8ee0"/>
    <polygon points="660,0 891,0 891,355 612,355 462,104" fill="url(#photoTone)" role="img" aria-label="Photo of hands reviewing growth charts on a desk with a magnifier, pencil and plant"/>
  </svg>
  <div class="brand"><span class="brand-mark"></span>Pixel Foundry</div>
  <div class="headline"><div class="l1">BUILD BRAND</div><div class="l2">SUSTAIN</div><div class="l3">GROWTH CURVE</div></div>
  <div class="contact">
    <svg class="icon" width="28" height="28" viewBox="0 0 28 28"><circle cx="14" cy="14" r="12" fill="none" stroke="#1a8ee0" stroke-width="2.5"/><path d="M9 8l3 0 1 4-2 1.5a8 8 0 0 0 3.5 3.5L16 15l4 1v3a1.5 1.5 0 0 1-1.5 1.5A11 11 0 0 1 7.5 9.5 1.5 1.5 0 0 1 9 8z" fill="#1a8ee0"/></svg>
    <span>(555) 274-0386</span><span class="divider"></span>
    <svg class="icon" width="26" height="26" viewBox="0 0 26 26"><circle cx="13" cy="13" r="11" fill="none" stroke="#1a8ee0" stroke-width="2.5"/><circle cx="13" cy="13" r="7" fill="#1a8ee0"/><path d="M6 13h14M13 6v14" stroke="#fff" stroke-width="1.2"/></svg>
    <span class="site">mypixelfoundry.example</span>
  </div>
</section>

<section class="scene">
  <div class="billboard">
    <div class="band"></div>
    <svg class="shape" width="891" height="355" viewBox="0 0 891 355">
      <defs><linearGradient id="photoTone2" x1="0" y1="0" x2="1" y2="1"><stop offset="0" stop-color="#f4f1f1"/><stop offset="1" stop-color="#dfe4e2"/></linearGradient></defs>
      <polygon points="615,0 410,96 580,355 600,355 445,100 655,0" fill="#0b2a78"/>
      <polygon points="640,0 430,98 596,355 616,355 458,102 670,0" fill="#1a8ee0"/>
      <polygon points="660,0 891,0 891,355 612,355 462,104" fill="url(#photoTone2)" role="img" aria-label="Photo of hands reviewing growth charts on a desk with a magnifier, pencil and plant"/>
    </svg>
    <div class="brand"><span class="brand-mark"></span>Pixel Foundry</div>
    <div class="headline"><div class="l1">BUILD BRAND</div><div class="l2">SUSTAIN</div><div class="l3">GROWTH CURVE</div></div>
    <div class="contact">
      <svg class="icon" width="28" height="28" viewBox="0 0 28 28"><circle cx="14" cy="14" r="12" fill="none" stroke="#1a8ee0" stroke-width="2.5"/><path d="M9 8l3 0 1 4-2 1.5a8 8 0 0 0 3.5 3.5L16 15l4 1v3a1.5 1.5 0 0 1-1.5 1.5A11 11 0 0 1 7.5 9.5 1.5 1.5 0 0 1 9 8z" fill="#1a8ee0"/></svg>
      <span>(555) 274-0386</span><span class="divider"></span>
      <svg class="icon" width="26" height="26" viewBox="0 0 26 26"><circle cx="13" cy="13" r="11" fill="none" stroke="#1a8ee0" stroke-width="2.5"/><circle cx="13" cy="13" r="7" fill="#1a8ee0"/><path d="M6 13h14M13 6v14" stroke="#fff" stroke-width="1.2"/></svg>
      <span class="site">mypixelfoundry.example</span>
    </div>
  </div>
</section>

</body>
</html>
```